Vorna Fleet business card

I am needing a business card that at a glance shows all the services that we provide emphasizing some more than others. We are a Fleet and Compliance management company as well as a software company. We provide outsourced solutions for KPX compliance and HR services via our own software.
In addition, we do
drug testing
GPS
Cameras
Electronic DVIRS
ELD's

Target Market(s)

Transportation company owners

Industry/Entity Type

Transportation supplier

Contact Information for Business Card

the card should inform potential customers what we do

Other font styles liked:
• I have added brand guidelines. See attached

Requirements
Must have
• See description
Should not have
• Colors outside my brand guide. See attached

```html
<!DOCTYPE html>
<html lang="en">
<head>
<meta charset="utf-8">
<title>Vorna Fleet business card</title>
<link href="https://fonts.googleapis.com/css2?family=Roboto:wght@400;500;700;900&display=swap" rel="stylesheet">
<style>
  :root{
    --bg:#2a2a2a;
    --brand-red:#c4161c;
    --deep-red:#8e0f16;
    --red-mid:#a8141b;
    --ink:#161616;
    --band:#141414;
    --paper:#f1f1f1;
    --paper-shade:#e2e2e2;
    --white:#ffffff;
    --text:#1e1e1e;
  }
  *{margin:0;padding:0;box-sizing:border-box}
  html,body{width:1200px;height:1138px;overflow:hidden}
  body{background:var(--bg);font-family:'Roboto',sans-serif;position:relative}
  .card{position:absolute;border-radius:14px;overflow:hidden;box-shadow:0 4px 10px rgba(0,0,0,.45)}

  /* front */
  .card-front{left:274px;top:186px;width:623px;height:376px;
    background:linear-gradient(135deg,var(--red-mid) 0%,var(--brand-red) 45%,var(--red-mid) 100%)}
  .front-name{position:absolute;left:0;right:0;top:70px;text-align:center;
    font-weight:900;font-size:72px;letter-spacing:-1px;color:var(--deep-red);line-height:1}
  .front-url{position:absolute;left:0;right:0;top:230px;text-align:center;
    font-size:16px;letter-spacing:9px;color:var(--ink)}
  .services-band{position:absolute;left:0;right:0;top:294px;height:61px;background:var(--band);text-align:center}
  .services-title{color:var(--brand-red);font-weight:500;font-size:16px;margin-top:9px}
  .services-list{color:#e8e8e8;font-size:16px;margin-top:3px}
  .services-list .sep{color:var(--brand-red);margin:0 6px}

  /* back */
  .card-back{left:275px;top:608px;width:619px;height:374px;
    background:linear-gradient(160deg,var(--paper) 0%,var(--paper-shade) 100%)}
  .back-name{position:absolute;left:39px;top:50px;font-weight:900;font-size:44px;
    letter-spacing:-1px;color:var(--ink);line-height:1}
  .back-name-mark{display:inline-block;width:14px;height:14px;background:var(--brand-red);margin-left:8px;vertical-align:middle}
  .person{position:absolute;left:39px;top:202px}
  .person-name{color:var(--brand-red);font-weight:700;font-size:27px;line-height:1.1}
  .person-role{color:var(--text);font-size:16px}
  .portrait{position:absolute;left:381px;top:32px;width:238px;height:228px;
    background:radial-gradient(ellipse at 55% 40%,#d9a98d 0%,#c4927a 35%,#9fb6c4 70%,rgba(233,233,233,0) 100%)}
  .divider{position:absolute;left:0;top:236px;width:619px;height:40px}
  .contacts{position:absolute;left:39px;top:270px;list-style:none}
  .contacts li{display:flex;align-items:center;height:26px;font-size:16px;color:var(--text)}
  .contacts svg{width:16px;height:16px;margin-right:16px}
  .contacts .accent{color:var(--brand-red)}
  .back-services{position:absolute;right:38px;top:298px;text-align:right;font-size:16px;color:var(--text);line-height:25px}
  .back-services .mark{color:var(--brand-red);margin:0 6px}
</style>
</head>
<body>
  <section class="card card-front">
    <div class="front-name">Vorna Fleet</div>
    <div class="front-url">www.vornafleet.com</div>
    <div class="services-band">
      <div class="services-title">OUR SERVICES:</div>
      <div class="services-list">Drug Testing<span class="sep">|</span>GPS<span class="sep">|</span>Cameras<span class="sep">|</span>Electronic DVIRS<span class="sep">|</span>ELD's</div>
    </div>
  </section>

  <section class="card card-back">
    <div class="back-name">Vorna Fleet<span class="back-name-mark"></span></div>
    <div class="portrait" role="img" aria-label="Portrait photo of the co-founder"></div>
    <svg class="divider" viewBox="0 0 619 40" aria-hidden="true">
      <path d="M145 14 H225 C250 14 255 28 285 28 H619" fill="none" stroke="var(--brand-red)" stroke-width="2"/>
    </svg>
    <div class="person">
      <div class="person-name">Dale Morrow</div>
      <div class="person-role">Co-Founder</div>
    </div>
    <ul class="contacts">
      <li><svg viewBox="0 0 16 16"><path d="M2 6c0-2 3-3 6-3s6 1 6 3l-2 1-1-2H5L4 7zM4 8h8l1 5H3z" fill="var(--brand-red)"/></svg>480-555-0182</li>
      <li><svg viewBox="0 0 16 16"><circle cx="8" cy="8" r="6.5" fill="none" stroke="var(--brand-red)" stroke-width="1.5"/><path d="M1.5 8h13M8 1.5c-3 3-3 10 0 13M8 1.5c3 3 3 10 0 13" fill="none" stroke="var(--brand-red)" stroke-width="1.2"/></svg>www.<span class="accent">vornafleet</span>.com</li>
      <li><svg viewBox="0 0 16 16"><rect x="1" y="3" width="14" height="10" fill="var(--brand-red)"/><path d="M1 3l7 6 7-6" fill="none" stroke="var(--white)" stroke-width="1.2"/></svg>dalemorrow@vornafleet.com</li>
    </ul>
    <div class="back-services">
      <div><span class="mark">»</span>Drug Testing<span class="mark">»</span>GPS<span class="mark">»</span>Cameras</div>
      <div><span class="mark">»</span>Electronic DVIRS<span class="mark">»</span>ELD's</div>
    </div>
  </section>
</body>
</html>
```